Creative, Modern and Conversion based Web Design

Kolvex Digital has recently launched a new logo and as part of our companies rebranding, we need a new website aimed towards the UK B2B marketplace.

The website needs to deliver a modern and creative website design whilst ensuring the design is tailored towards conversion optimisation.

This site must drive point of contact either from an online form, via a direct telephone call or Skype connection.

Our sales are all offline so the website will be a simple, elegant and stunning information portal.

Kolvex Digital offers Digital Marketing services to companies throughout the UK - our target audiences are companies that turnover a minimum of 3 million pounds a year and as such we need to deliver a professional image that installs confidence in our companies abilities.

We do not like websites that are reliant upon stock photography - we are happy for stock photography to be used in a small way however the site must not look like a template filled with stock photography.

What do we do

We supply digital marketing services to those companies who demand a strong return on investment - our company prides itself on delivering successful campaigns that help establish long-term profitable relationships.

A lot of the information presented on our old site is relevant today however the design sucks. So please use the information on our current website as a foundation for your design content.

I am looking for several page designs including

"Home Page" Desktop Version
"Service Page" Desktop Version
"Blog Page" Desktop Version

"Home Page" Mobile Version
"Service Page" Mobile Version
"Blog Page" Mobile Version

In the 1st instance please only submit a single design for the "Home Page" Desktop Version - those designers that we are impressed with will be asked to complete the other designs before a winner is selected.

I like modern clean fonts - the site needs to welcome the reader and encourage them to absorb the information - not to overload and make them leave.

The site must be designed to naturally fit our companies new logo.

NO TEMPLATES

Target Market(s)

B2b - 3 million turnover and above

Industry/Entity Type

Digital Marketing

Number of Pages Required

3 page

Requirements
Must have
• Blended well with the companies logo
• We need conversion optimisation to be a huge part of the design - we considered a conversation when a potential customer reaches out to use via - web form, telephone or skype
• The current content on the old website fits today's business but the design sucks.
• www.kolvexdigital-example.com
Nice to have
• We need 3 pages (in 2 variants Desktop and Mobile)
• Home Page
• Service Page
• Blog Page
• Please only deliver the "Home Page" desktop version - if we are happy with your design we will aks for the additional pages
Should not have
• No templates and not stock photo heavy design

```html
<!DOCTYPE html>
<html lang="en">
<head>
<meta charset="utf-8">
<title>Kolvex Digital – Search marketing that actually delivers</title>
<link rel="stylesheet" href="https://fonts.googleapis.com/css2?family=Poppins:wght@300;400;500;600;700&display=swap">
<style>
:root{
  --blue:#0f4f9f;
  --blue-band:#1358ab;
  --blue-wave:#1f66b8;
  --pale:#e8eef7;
  --pale-2:#f1f5fb;
  --ink:#1d1d1f;
  --text:#555a60;
  --muted:#9aa0a6;
  --line:#e2e4e8;
  --dark:#454545;
  --white:#ffffff;
  --footer:#1f4f95;
}
*{box-sizing:border-box;margin:0;padding:0}
html,body{width:1200px;height:4018px;overflow:hidden}
body{font-family:'Poppins',sans-serif;color:var(--text);background:var(--white);position:relative}
.abs{position:absolute}
a{color:inherit;text-decoration:none}
.btn{display:inline-block;border:2px solid var(--ink);border-radius:30px;padding:12px 24px;font-size:12px;font-weight:600;letter-spacing:.5px;text-transform:uppercase;color:var(--ink)}
.btn--light{border-color:var(--white);color:var(--white)}

/* header */
.site-header{left:0;top:0;width:1200px;height:100px;display:flex;align-items:center;justify-content:space-between;padding:0 94px 0 86px}
.brand{display:flex;align-items:center;gap:12px;font-size:22px;font-weight:600;color:var(--ink)}
.brand__mark{width:22px;height:22px;background:#6b6f75}
.nav{display:flex;gap:36px;font-size:12px;font-weight:600;text-transform:uppercase;color:var(--ink)}

/* hero */
.hero{left:0;top:100px;width:1200px;height:618px;background:var(--pale)}
.hero__photo{position:absolute;left:520px;top:0;width:680px;height:618px;background:linear-gradient(135deg,#d9dde2 0%,#b9c0c8 45%,#8c8f93 100%)}
.hero__card{left:120px;top:255px;width:430px;height:308px;background:var(--white);padding:98px 40px 0 40px;box-shadow:0 10px 30px rgba(0,0,0,.05)}
.hero__title{font-size:38px;font-weight:300;line-height:1.25;color:var(--ink)}
.hero__lead{margin-top:20px;font-size:16px;line-height:1.6;color:var(--text)}

/* tools */
.tools{left:0;top:718px;width:1200px;height:127px;display:flex;align-items:center;justify-content:space-around;padding:0 90px;border-bottom:1px solid var(--line)}
.tools span{font-size:20px;font-weight:500;color:#6f747a}

/* roi */
.roi{left:0;top:845px;width:1200px;height:270px}
.roi__title{left:94px;top:36px;width:430px;font-size:35px;font-weight:700;line-height:1.25;color:var(--ink)}
.roi__accent{left:94px;top:170px;font-size:26px;font-weight:600;color:var(--blue)}
.roi__copy{left:555px;top:36px;width:560px;font-size:14.5px;line-height:1.7}
.roi__copy a{color:var(--blue)}

/* in-house band */
.inhouse{left:0;top:1138px;width:785px;height:188px;background:var(--dark);padding:44px 0 0 94px;color:var(--white)}
.inhouse h2{font-size:28px;font-weight:600}
.inhouse p{margin-top:8px;font-size:14px;color:#d7d7d7}
.inhouse .btn{margin-top:22px;padding:10px 20px;font-size:11px}
.inhouse-edge{left:1107px;top:1138px;width:93px;height:188px;background:var(--dark)}
.badge{left:845px;top:1150px;width:240px;height:160px;border:2px solid var(--line);border-radius:10px;background:var(--pale-2)}

/* services */
.services{left:0;top:1380px;width:1200px;height:400px;text-align:center}
.services__kicker{font-size:14px;color:var(--text)}
.services__title{margin-top:6px;font-size:28px;font-weight:700;color:var(--blue)}
.services__grid{position:absolute;left:115px;top:150px;width:970px;display:grid;grid-template-columns:repeat(3,1fr)}
.service{padding:0 40px;border-right:1px solid var(--line)}
.service:last-child{border-right:none}
.service svg{width:62px;height:62px}
.service h3{margin-top:18px;font-size:14px;font-weight:700;color:var(--ink);text-transform:uppercase}
.service p{margin-top:18px;font-size:14px;line-height:1.65}
.arrow-box{position:absolute;top:265px;width:30px;height:40px;border:1px solid #b0b4b9;display:flex;align-items:center;justify-content:center}

/* stats */
.stats-bg{left:0;top:1760px;width:1200px;height:600px}
.monitor{left:94px;top:2010px;width:394px;height:280px}
.monitor__screen{position:absolute;left:0;top:0;width:394px;height:232px;background:#1a1a1a;padding:10px;border-radius:6px}
.monitor__display{width:100%;height:100%;background:linear-gradient(90deg,#f6f4fb 0%,#efe3f4 40%,#f5d9e4 70%,#f8f1d8 100%)}
.monitor__stand{position:absolute;left:0;top:232px;width:394px;height:40px;background:#dfe1e4;border-radius:0 0 6px 6px}
.stats__title{left:528px;top:2022px;font-size:30px;font-weight:600;line-height:1.35;color:var(--ink)}
.stat{top:2140px;width:200px;text-align:left}
.stat svg{width:70px;height:70px}
.stat__num{font-size:46px;font-weight:700;color:#2f78c4;line-height:1.1}
.stat__label{font-size:14px;color:var(--text)}

/* testimonial */
.testimonial{left:0;top:2362px;width:1200px;height:322px;background:var(--blue-band);overflow:hidden;color:var(--white)}
.testimonial svg.wave{position:absolute;left:0;bottom:0;width:1200px;height:200px}
.testimonial h2{position:absolute;left:180px;top:72px;font-size:22px;font-weight:600;padding-bottom:8px;border-bottom:2px solid var(--white)}
.testimonial blockquote{position:absolute;left:180px;top:148px;width:840px;font-size:16px;line-height:1.6}
.testimonial cite{position:absolute;left:180px;top:262px;font-style:normal;font-size:13px;font-weight:700;text-transform:uppercase}
.testimonial .chev{position:absolute;top:140px;font-size:34px;font-weight:300}

/* handle seo */
.handle{left:161px;top:2780px;width:740px}
.handle h2{font-size:31px;font-weight:500;color:var(--ink)}
.handle h3{margin-top:4px;font-size:15px;font-weight:600;color:var(--ink)}
.handle p{margin-top:22px;font-size:14.5px;line-height:1.65}
.handle-btn{left:911px;top:2878px}

/* process */
.process__title{left:0;top:3046px;width:1200px;text-align:center;font-size:22px;font-weight:600;color:var(--ink)}
.process{left:112px;top:3075px;width:1000px;height:330px;display:grid;grid-template-columns:228px 210px 308px 254px}
.step{padding:0 20px 0 0;border-right:1px solid var(--line);margin-right:20px}
.step:last-child{border-right:none;margin-right:0}
.step__num{font-size:50px;font-weight:300;color:#c9ccd1;line-height:1.2}
.step p{margin-top:4px;font-size:14px;line-height:1.65}

/* cta */
.cta-bg{left:0;top:3440px;width:1200px;height:405px}
.cta{left:0;top:3570px;width:1200px;text-align:center}
.cta h2{font-size:42px;font-weight:700;color:var(--blue)}
.cta p{margin-top:10px;font-size:16px}
.cta .btn{margin-top:26px}

/* contact strip */
.contact{left:0;top:3845px;width:1200px;height:133px;background:var(--pale-2);display:flex;align-items:center;padding-left:150px;gap:0}
.contact__item{display:flex;align-items:center;gap:16px;width:300px}
.contact__item svg{width:40px;height:40px}
.contact__label{font-size:13px;font-weight:600;color:var(--ink);text-transform:uppercase}
.contact__value{font-size:13px;color:var(--text)}
.legal{left:0;top:3978px;width:1200px;height:40px;background:var(--footer);color:#d9e3f2;font-size:12px;display:flex;align-items:center;justify-content:center}
</style>
</head>
<body>

<header class="site-header abs">
  <div class="brand"><span class="brand__mark"></span>Kolvex Digital</div>
  <nav class="nav">
    <a>Home</a><a>About Us</a><a>Our Services</a><a>White Label Link Building</a><a>Blog</a><a>Contact Us</a>
  </nav>
</header>

<section class="hero abs">
  <div class="hero__photo" role="img" aria-label="Photo of a marketing team reviewing documents at a bright office desk"></div>
</section>
<div class="hero__card abs">
  <h1 class="hero__title">Search marketing that actually delivers</h1>
  <p class="hero__lead">Search marketing is our forte. Our client results highlight just how good we do it.</p>
</div>

<div class="tools abs">
  <span>Metricly</span><span>RankScope</span><span>Authora</span><span>HeatTrail</span><span>AdLedger</span><span>Searchwell</span>
</div>

<section class="roi abs">
  <h2 class="roi__title abs">Do you want to see an enviable ROI on search marketing?</h2>
  <p class="roi__accent abs">It's possible – you've found us.</p>
  <p class="roi__copy abs">We know and understand the world of business. We know that ROI is the single most important metric in the marketing world. We've worked within some of the world's largest industries – such as finance, insurance, payday loans and health; where achieving above 100% ROI is often impossible. For us, it's just a challenge that can be overcome. Whether we're working with you to drive your <a>Pay-Per-Click Marketing</a>, <a>Organic Search Marketing (SEO)</a>, Email Marketing or <a>Lead Filtering &amp; Delivery</a> – we always have your ROI in mind. That's why we're known as the ROI driven digital agency.</p>
</section>

<section class="inhouse abs">
  <h2>Handle your SEO in-house?</h2>
  <p>Consider using our industry-leading link outreach service to bolster your efforts.</p>
  <a class="btn btn--light">Contact us now</a>
</section>
<div class="badge abs" role="img" aria-label="Partner certification badge"></div>
<div class="inhouse-edge abs"></div>

<section class="services abs">
  <p class="services__kicker">We can cover all the aspects of your digital marketing needs</p>
  <h2 class="services__title">We Are Specialized in the Following Services</h2>
  <div class="arrow-box" style="left:55px"><svg width="10" height="14" viewBox="0 0 10 14"><path d="M8 1 2 7l6 6" fill="none" stroke="#555" stroke-width="1.5"/></svg></div>
  <div class="services__grid">
    <article class="service">
      <svg viewBox="0 0 62 62"><rect x="8" y="10" width="42" height="32" fill="none" stroke="#222" stroke-width="2.5"/><path d="M14 34l9-9 7 6 12-12" fill="none" stroke="#222" stroke-width="2.5"/><circle cx="44" cy="44" r="8" fill="none" stroke="#222" stroke-width="2.5"/><path d="M50 50l7 7" stroke="#222" stroke-width="3"/></svg>
      <h3>Organic Search</h3>
      <p>Attract traffic that converts and interacts with your brand through Organic. We implement both short-term and long-term campaigns to bolster your success.</p>
    </article>
    <article class="service">
      <svg viewBox="0 0 62 62"><path d="M8 54h48" stroke="#222" stroke-width="2.5"/><rect x="12" y="38" width="7" height="16" fill="none" stroke="#222" stroke-width="2.5"/><rect x="24" y="30" width="7" height="24" fill="none" stroke="#222" stroke-width="2.5"/><rect x="36" y="22" width="7" height="32" fill="none" stroke="#222" stroke-width="2.5"/><circle cx="48" cy="14" r="7" fill="none" stroke="#222" stroke-width="2.5"/><path d="M10 30 28 14" stroke="#222" stroke-width="2.5"/></svg>
      <h3>Paid Search</h3>
      <p>Drive highly converting traffic to your website. Our PPC campaigns are ROI-driven from the start – helping you to scale your business quickly.</p>
    </article>
    <article class="service">
      <svg viewBox="0 0 62 62"><path d="M12 44 26 26 38 36 52 16" fill="none" stroke="#222" stroke-width="2.5"/><circle cx="12" cy="44" r="5" fill="#fff" stroke="#222" stroke-width="2.5"/><circle cx="26" cy="26" r="5" fill="#fff" stroke="#222" stroke-width="2.5"/><circle cx="38" cy="36" r="5" fill="#fff" stroke="#222" stroke-width="2.5"/><circle cx="52" cy="16" r="5" fill="#fff" stroke="#222" stroke-width="2.5"/></svg>
      <h3>Link Outreach</h3>
      <p>The core foundation of any search campaign. Our team of link outreachers are the best in the industry. We secure link placements that drive rankings.</p>
    </article>
  </div>
  <div class="arrow-box" style="left:1115px"><svg width="10" height="14" viewBox="0 0 10 14"><path d="M2 1l6 6-6 6" fill="none" stroke="#555" stroke-width="1.5"/></svg></div>
</section>

<svg class="stats-bg abs" viewBox="0 0 1200 600" preserveAspectRatio="none" aria-hidden="true"><polygon points="0,20 120,0 560,600 0,600" fill="#eef2f9"/></svg>
<div class="monitor abs">
  <div class="monitor__screen"><div class="monitor__display" role="img" aria-label="Area chart illustration titled Grow your online business with us"></div></div>
  <div class="monitor__stand"></div>
</div>
<h2 class="stats__title abs">We grow as our clients grow.<br>That's what we love</h2>
<div class="stat abs" style="left:536px">
  <svg viewBox="0 0 70 70"><rect x="10" y="14" width="50" height="40" rx="4" fill="none" stroke="#3a7fc8" stroke-width="2.5"/><path d="M20 42l10-10 8 6 12-14" fill="none" stroke="#3a7fc8" stroke-width="2.5"/></svg>
  <div class="stat__num">117</div><div class="stat__label">Satisfied Clients</div>
</div>
<div class="stat abs" style="left:777px">
  <svg viewBox="0 0 70 70"><rect x="10" y="16" width="50" height="38" rx="4" fill="none" stroke="#3a7fc8" stroke-width="2.5"/><path d="M24 34l8 8 16-16" fill="none" stroke="#3a7fc8" stroke-width="2.5"/></svg>
  <div class="stat__num">215</div><div class="stat__label">Campaigns Finished</div>
</div>
<div class="stat abs" style="left:990px">
  <svg viewBox="0 0 70 70"><path d="M16 26h32v20a12 12 0 0 1-12 12h-8a12 12 0 0 1-12-12z" fill="none" stroke="#3a7fc8" stroke-width="2.5"/><path d="M48 30h6a6 6 0 0 1 0 12h-6" fill="none" stroke="#3a7fc8" stroke-width="2.5"/><path d="M26 10v10M34 10v10" stroke="#3a7fc8" stroke-width="2.5"/></svg>
  <div class="stat__num">1798</div><div class="stat__label">Cups of Coffee</div>
</div>

<section class="testimonial abs">
  <svg class="wave" viewBox="0 0 1200 200" preserveAspectRatio="none" aria-hidden="true"><path d="M0 120 C150 60 260 150 420 90 S700 40 860 110 1080 60 1200 90 V200 H0Z" fill="#1d62b4"/><path d="M0 160 C200 110 380 190 600 140 S960 120 1200 150 V200 H0Z" fill="#1a5eb0"/></svg>
  <h2>Our Customers Feeback</h2>
  <span class="chev" style="left:118px">‹</span>
  <blockquote>My company has had a very noticeable positive growth in organic traffic and rankings since they were brought on board. The team that has been assigned my site continues to demonstrate great communication and knowledge regarding not only link building, but also on and off-site SEO practices as well.</blockquote>
  <cite>Daniel Hart</cite>
  <span class="chev" style="left:1066px">›</span>
</section>

<section class="handle abs">
  <h2>Handle SEO Yourself? Perfect.</h2>
  <h3>Hassle-Free Link Placements That Drive Rankings</h3>
  <p>Our link placements are used by some of the world's largest companies in the most difficult industries – such as payday loans, insurance, finance, health and legal. We use our link placement service in conjunction with our Organic Search (SEO) offerings; although some of our clients handle their SEO in-house and prefer to use our link placements to bolster their rankings.</p>
</section>
<a class="btn handle-btn abs">Get started now</a>

<h2 class="process__title abs">Here's how our unique, link acquisition process works:</h2>
<section class="process abs">
  <div class="step"><div class="step__num">01</div><p>We take your clients URLs and their business sector (or your own sites), and we utilise our connections to try and secure a link placement.</p></div>
  <div class="step"><div class="step__num">02</div><p>All of the sites we outreach too are 100% genuine – we do not own nor control any of the sites.</p></div>
  <div class="step"><div class="step__num">03</div><p>If a webmaster chooses to link to you, it is of their own accord. They have decided to link to you. Thus, you have earned a genuine link.</p></div>
  <div class="step"><div class="step__num">04</div><p>We will identify the most relevant page/post on their site, and work with the webmaster to weave your links into their existing content. We will write an additional sentence or two to make sure the anchor text fits in with the content.</p></div>
</section>

<svg class="cta-bg abs" viewBox="0 0 1200 405" preserveAspectRatio="none" aria-hidden="true"><path d="M0 80 C250 0 420 40 640 70 S1000 60 1200 20 V405 H0Z" fill="#eef2f9"/></svg>
<section class="cta abs">
  <h2>Want To Improve Your ROI? Let's Talk</h2>
  <p>We'll never turn down an opportunity to discover how we can help grow your business.</p>
  <a class="btn">Contact us today</a>
</section>

<footer class="contact abs">
  <div class="contact__item">
    <svg viewBox="0 0 40 40"><rect x="4" y="9" width="32" height="22" fill="none" stroke="#222" stroke-width="2"/><path d="M4 9l16 13 16-13" fill="none" stroke="#222" stroke-width="2"/></svg>
    <div><div class="contact__label">Mail us:</div><div class="contact__value">info@kolvexdigital-example.com</div></div>
  </div>
  <div class="contact__item">
    <svg viewBox="0 0 40 40"><path d="M10 5l7 8-4 4c2 4 6 8 10 10l4-4 8 7-4 6C18 35 5 22 4 9z" fill="none" stroke="#222" stroke-width="2"/></svg>
    <div><div class="contact__label">Call us:</div><div class="contact__value">01632 960418</div></div>
  </div>
  <div class="contact__item">
    <svg viewBox="0 0 40 40"><circle cx="20" cy="20" r="15" fill="none" stroke="#222" stroke-width="2"/><path d="M20 10v10l7 5" fill="none" stroke="#222" stroke-width="2"/></svg>
    <div><div class="contact__label">Working hours</div><div class="contact__value">9AM-5PM, MON-FRI</div></div>
  </div>
</footer>
<div class="legal abs">© 2018 Kolvex Digital Limited. All rights reserved.</div>

</body>
</html>
```